Business Card Design - Law Firm

We are a boutique law firm located near the beach in Manly, Australia. We have recently had a new logo designed and are revamping our business cards with the new logo.

We have recently had a business card design done for us but are not entirely happy with it. We are looking for something modern, simplistic but striking. We would like to see multiple designs.

We have attached a word document which includes our new logo and the current business card design which we are looking at moving away from.

We would like the business cards to be double sided. We would like the design to include something which we can print in gloss colour when we send it to the business card printers.

```html
<!DOCTYPE html>
<html lang="en">
<head>
<meta charset="utf-8">
<title>Harwick &amp; Partners – Business Cards</title>
<link rel="stylesheet" href="https://fonts.googleapis.com/css2?family=Montserrat:wght@300;400;600;700&display=swap">
<style>
  :root {
    --navy: #2f3b85;
    --gold: #b5a26a;
    --white: #ffffff;
    --ink: #1a1a1a;
    --stage: #d9d9d9;
  }
  * { margin: 0; padding: 0; box-sizing: border-box; }
  html, body { width: 1200px; height: 1200px; overflow: hidden; background: var(--stage); }
  body { font-family: "Montserrat", sans-serif; position: relative; }

  .card {
    position: absolute;
    left: 180px;
    width: 840px;
    height: 480px;
    border-radius: 28px;
    overflow: hidden;
    box-shadow: 0 14px 30px rgba(0,0,0,0.25);
  }
  .card--front { top: 90px; background: var(--navy); }
  .card--back { top: 630px; background: var(--white); }

  .wordmark {
    position: absolute;
    display: flex;
    align-items: center;
    gap: 14px;
    font-weight: 600;
    font-size: 34px;
    letter-spacing: 2px;
    white-space: nowrap;
  }
  .wordmark__dot { width: 16px; height: 16px; border-radius: 50%; background: currentColor; }
  .card--front .wordmark { color: var(--white); left: 50%; top: 50%; transform: translate(-50%, -50%); }
  .card--back .wordmark { color: var(--ink); font-size: 24px; left: 60px; top: 224px; }

  .back-shape { position: absolute; inset: 0; width: 840px; height: 480px; }

  .contact {
    position: absolute;
    left: 572px;
    top: 96px;
    color: var(--white);
  }
  .contact__name { color: var(--gold); font-weight: 700; font-size: 22px; letter-spacing: 0.5px; }
  .contact__title { font-weight: 300; font-size: 14px; margin-top: 2px; }
  .contact__rule { width: 50px; height: 3px; background: var(--gold); margin: 14px 0 14px; }
  .contact__address { font-weight: 600; font-size: 12px; line-height: 1.4; margin-bottom: 12px; }
  .contact__line { display: flex; align-items: center; gap: 7px; font-weight: 600; font-size: 12px; line-height: 1.7; white-space: nowrap; }
  .contact__line svg { width: 12px; height: 12px; flex: none; }
</style>
</head>
<body>

<section class="card card--front" aria-label="Card front">
  <div class="wordmark"><span class="wordmark__dot"></span>Harwick &amp; Partners</div>
</section>

<section class="card card--back" aria-label="Card back">
  <svg class="back-shape" viewBox="0 0 840 480" aria-hidden="true">
    <path d="M345 0 C330 100 390 180 490 220 C540 245 565 360 575 480 H840 V0 Z" fill="var(--navy)"/>
    <path d="M462 228 C515 255 540 370 552 480" fill="none" stroke="var(--gold)" stroke-width="8"/>
  </svg>

  <div class="wordmark"><span class="wordmark__dot"></span>Harwick &amp; Partners</div>

  <div class="contact">
    <div class="contact__name">NINA CALDER</div>
    <div class="contact__title">Practice Manager</div>
    <div class="contact__rule"></div>
    <div class="contact__address">Suite 4, 12 Marlin Street<br>CORAL BAY NSW 2101</div>
    <div class="contact__line">
      <svg viewBox="0 0 24 24"><path fill="var(--gold)" d="M6.6 10.8a15 15 0 0 0 6.6 6.6l2.2-2.2a1 1 0 0 1 1-.25 11.4 11.4 0 0 0 3.6.57 1 1 0 0 1 1 1V20a1 1 0 0 1-1 1A17 17 0 0 1 3 4a1 1 0 0 1 1-1h3.5a1 1 0 0 1 1 1c0 1.25.2 2.45.57 3.57a1 1 0 0 1-.25 1z"/></svg>
      (02) 5550 1834
    </div>
    <div class="contact__line">
      <svg viewBox="0 0 24 24"><rect x="2" y="5" width="20" height="14" rx="2" fill="var(--gold)"/><path d="M3 6l9 7 9-7" fill="none" stroke="var(--navy)" stroke-width="2"/></svg>
      nina.calder@coralbaylaw.com.au
    </div>
    <div class="contact__line">
      <svg viewBox="0 0 24 24" fill="none" stroke="var(--gold)" stroke-width="2"><circle cx="12" cy="12" r="9"/><path d="M3 12h18M12 3c3 3 3 15 0 18M12 3c-3 3-3 15 0 18"/></svg>
      www.harwickpartners.com.au
    </div>
  </div>
</section>

</body>
</html>
```